Most captivating card ever!

Life Coach - Professional Adventurer - Entrepreneur
I need the worlds most amazing business card for my personal brand. This business card will mostly be used to give to prospective clients for life coaching and business coaching.
Be creative, be adventurous. It needs to stand out. Make people say.. I need this guy!
My background is as an entrepreneur and professional adventurer undertaking extreme expeditions. I am now moving into life coaching.
No specific design ideas, so you have full creativity. Show me your best.
Industry/Entity Type
Life Coaching
Contact Information for Business Card
Dan Pellow
itsdanp.com.au
0468215903
Colors
Designer to choose colors to be used in the design.
Look and feel

```html
<!DOCTYPE html>
<html lang="en">
<head>
<meta charset="utf-8">
<title>Dan Pellow – Business Card</title>
<link rel="stylesheet" href="https://fonts.googleapis.com/css2?family=Jost:ital,wght@0,700;1,300&display=swap">
<style>
  :root {
    --ink: #ffffff;
    --rule: rgba(255, 255, 255, 0.35);
    --ember: #d2643a;
    --amber: #d98a45;
    --haze: #b88a55;
    --sea: #5a6255;
    --deep: #3a453e;
  }
  * { margin: 0; padding: 0; box-sizing: border-box; }
  html, body {
    width: 734px;
    height: 1200px;
    overflow: hidden;
    background: #222;
  }
  .card {
    position: relative;
    width: 734px;
    height: 1200px;
    overflow: hidden;
    font-family: "Jost", "Futura", sans-serif;
    color: var(--ink);
  }
  .card__photo {
    position: absolute;
    inset: 0;
    background: linear-gradient(180deg, var(--ember) 0%, var(--amber) 40%, var(--haze) 65%, var(--sea) 85%, var(--deep) 100%);
  }
  .card__content {
    position: absolute;
    left: 102px;
    top: 0;
    right: 0;
  }
  .name {
    position: absolute;
    top: 372px;
    left: 0;
    font-weight: 700;
    font-size: 78px;
    line-height: 78px;
    letter-spacing: 1px;
  }
  .name span { display: block; }
  .roles {
    position: absolute;
    top: 605px;
    left: 0;
    width: 510px;
    list-style: none;
  }
  .roles li {
    font-style: italic;
    font-weight: 300;
    font-size: 44px;
    line-height: 80px;
    height: 80px;
    letter-spacing: 0.5px;
    border-bottom: 1px solid var(--rule);
  }
  .roles li:last-child { border-bottom: none; }
  .contact {
    position: absolute;
    top: 916px;
    left: -4px;
    list-style: none;
  }
  .contact li {
    display: flex;
    align-items: center;
    height: 76px;
    font-weight: 700;
    font-size: 44px;
    letter-spacing: 0.5px;
  }
  .contact svg { flex: none; }
  .contact__web svg { margin-right: 30px; }
  .contact__phone svg { margin: 0 34px 0 10px; }
</style>
</head>
<body>
  <div class="card">
    <div class="card__photo" role="img" aria-label="Photograph of a wave crashing against a sea cliff at sunset"></div>
    <div class="card__content">
      <h1 class="name"><span>DAN</span><span>Pellow</span></h1>
      <ul class="roles">
        <li>Life Coach</li>
        <li>Professional Adventurer</li>
        <li>Entrepreneur</li>
      </ul>
      <ul class="contact">
        <li class="contact__web">
          <svg width="48" height="40" viewBox="0 0 48 40" aria-hidden="true">
            <rect x="2" y="2" width="44" height="28" fill="none" stroke="#fff" stroke-width="4"/>
            <rect x="20" y="30" width="8" height="6" fill="#fff"/>
            <rect x="12" y="35" width="24" height="4" fill="#fff"/>
          </svg>
          itsdanp.com.au
        </li>
        <li class="contact__phone">
          <svg width="26" height="50" viewBox="0 0 26 50" aria-hidden="true">
            <rect x="2" y="2" width="22" height="46" rx="4" fill="none" stroke="#fff" stroke-width="3"/>
            <line x1="2" y1="9" x2="24" y2="9" stroke="#fff" stroke-width="2"/>
            <line x1="2" y1="40" x2="24" y2="40" stroke="#fff" stroke-width="2"/>
            <circle cx="13" cy="44" r="1.8" fill="#fff"/>
          </svg>
          0468 215 903
        </li>
      </ul>
    </div>
  </div>
</body>
</html>
```